Business Card for Inovative Flexible Packaging Company

Create a business card that is both simple and stricking at the same time.
Preferably only one color (orange) or two colors (black and orange).
Information to print:
Corvela, Lda
[T] 22 418 6093
[M] 91 362 7148
[F] 22 418 6057
[@] corvela.mt@tarnomail.example
SEDE & ARMAZÉM
Rua Dos Vimieiros do Outeiro, 317
Serzedo
4410-862 Serzedo - VN Gaia
PORTUGAL
Reason: A lot of the ideas are obvious. I want something different. Inovative. dare to do something eye catching with style.
Business Consumers. Packaging Designers.
Business

```html
<!DOCTYPE html>
<html lang="pt">
<head>
<meta charset="utf-8">
<title>Corvela – Cartão de Visita</title>
<link href="https://fonts.googleapis.com/css2?family=Lora:wght@400;600&display=swap" rel="stylesheet">
<style>
  :root {
    --board: #ececee;
    --card: #ffffff;
    --orange: #f2511b;
    --ink: #1a1a1a;
    --shadow: rgba(0, 0, 0, 0.45);
  }
  html, body {
    margin: 0;
    padding: 0;
    width: 1200px;
    height: 900px;
    overflow: hidden;
    background: var(--board);
    font-family: "Lora", Georgia, serif;
    color: var(--ink);
  }
  .board {
    position: relative;
    width: 1200px;
    height: 900px;
  }
  .card {
    position: absolute;
    top: 177px;
    width: 542px;
    height: 311px;
    background: var(--card);
    box-shadow: 6px 6px 6px var(--shadow);
    overflow: hidden;
  }
  .card--front { left: 48px; }
  .card--back { left: 632px; }

  .wordmark {
    display: flex;
    align-items: center;
    color: var(--orange);
    font-weight: 600;
    line-height: 1;
  }
  .wordmark__square {
    background: var(--orange);
    flex: none;
  }

  .card--front .wordmark {
    position: absolute;
    left: 0;
    right: 0;
    top: 128px;
    justify-content: center;
    font-size: 56px;
    gap: 16px;
  }
  .card--front .wordmark__square { width: 50px; height: 50px; }

  .stripe {
    position: absolute;
    display: block;
  }
  .stripe--top { left: 0; top: 0; }
  .stripe--bottom { right: 0; bottom: 0; }

  .card--back .wordmark {
    position: absolute;
    left: 22px;
    top: 28px;
    font-size: 34px;
    gap: 10px;
  }
  .card--back .wordmark__square { width: 34px; height: 34px; }

  .company {
    position: absolute;
    left: 43px;
    top: 130px;
    margin: 0;
    font-size: 18px;
    font-weight: 400;
  }
  .contacts {
    position: absolute;
    left: 43px;
    top: 164px;
    margin: 0;
    padding: 0;
    list-style: none;
    font-size: 14px;
  }
  .contacts li {
    display: flex;
    align-items: center;
    gap: 6px;
    height: 23.5px;
    white-space: nowrap;
  }
  .contacts svg { width: 12px; height: 12px; fill: var(--orange); flex: none; }

  .address {
    position: absolute;
    left: 292px;
    top: 155px;
    margin: 0;
    font-style: normal;
    font-size: 14px;
    line-height: 20.5px;
    white-space: nowrap;
  }

  .board > .wordmark {
    position: absolute;
    left: 826px;
    top: 790px;
    font-size: 62px;
    gap: 16px;
  }
  .board > .wordmark .wordmark__square { width: 60px; height: 60px; }
</style>
</head>
<body>
<main class="board">

  <section class="card card--front" aria-label="Frente do cartão">
    <div class="wordmark"><span class="wordmark__square"></span>Corvela</div>
  </section>

  <section class="card card--back" aria-label="Verso do cartão">
    <svg class="stripe stripe--top" width="380" height="16" viewBox="0 0 380 16" aria-hidden="true">
      <polygon points="0,0 374,0 368,6 0,6" fill="var(--ink)"/>
      <polygon points="0,9 360,9 354,14 0,14" fill="var(--orange)"/>
    </svg>

    <div class="wordmark"><span class="wordmark__square"></span>Corvela</div>

    <h1 class="company">Corvela, Lda</h1>
    <ul class="contacts">
      <li>
        <svg viewBox="0 0 24 24"><path d="M6.6 10.8a15 15 0 0 0 6.6 6.6l2.2-2.2c.3-.3.7-.4 1-.2 1.1.4 2.3.6 3.6.6.6 0 1 .4 1 1V20c0 .6-.4 1-1 1A17 17 0 0 1 3 4c0-.6.4-1 1-1h3.5c.6 0 1 .4 1 1 0 1.3.2 2.5.6 3.6.1.3 0 .7-.2 1z"/></svg>
        22 418 6093
      </li>
      <li>
        <svg viewBox="0 0 24 24"><path d="M7 1h10a2 2 0 0 1 2 2v18a2 2 0 0 1-2 2H7a2 2 0 0 1-2-2V3a2 2 0 0 1 2-2zm0 3v13h10V4z"/></svg>
        91 362 7148
      </li>
      <li>
        <svg viewBox="0 0 24 24"><path d="M7 2h10v6H7zM3 9h18v10h-3v3H6v-3H3zm5 6v5h8v-5z"/></svg>
        22 418 6057
      </li>
      <li>
        <svg viewBox="0 0 24 24"><path d="M2 5h20v14H2zm2 2v.5l8 5 8-5V7z"/></svg>
        corvela.mt@tarnomail.example
      </li>
    </ul>

    <address class="address">
      SEDE &amp; ARMAZÉM<br>
      Rua Dos Vimieiros do Outeiro, 317<br>
      Serzedo<br>
      4410-862 Serzedo - VN Gaia<br>
      PORTUGAL
    </address>

    <svg class="stripe stripe--bottom" width="376" height="16" viewBox="0 0 376 16" aria-hidden="true">
      <polygon points="10,2 376,2 376,7 6,7" fill="var(--orange)"/>
      <polygon points="4,10 376,10 376,16 0,16" fill="var(--ink)"/>
    </svg>
  </section>

  <div class="wordmark"><span class="wordmark__square"></span>Corvela</div>

</main>
</body>
</html>
```